Cascadia Rhythm Guild Business Cards

The Cascadia Rhythm Guild is a non-profit organization that supports, promotes, and manages music events in the Pacific Northwest. Our mission is to keep the blues alive. We do this by partnering with local venues, schools, and national acts to bring some of the best blues music to our members. As newly elected Executive Board Members we would like to have new business cards designed. I have included a copy of our logo.

```html
<!DOCTYPE html>
<html lang="en">
<head>
<meta charset="utf-8">
<title>Cascadia Rhythm Guild Business Cards</title>
<link href="https://fonts.googleapis.com/css2?family=Tinos:wght@400;700&display=swap" rel="stylesheet">
<style>
  :root {
    --backdrop: #2a2a2a;
    --card: #050505;
    --accent: #e0461c;
    --accent-deep: #c2330f;
    --ink: #ffffff;
    --ink-soft: #e6e6e6;
  }
  * { margin: 0; padding: 0; box-sizing: border-box; }
  html, body {
    width: 1200px;
    height: 1108px;
    overflow: hidden;
    background: var(--backdrop);
    font-family: "Tinos", "Times New Roman", serif;
  }
  .sheet {
    position: relative;
    width: 1200px;
    height: 1108px;
  }
  .card {
    position: absolute;
    top: 224px;
    width: 390px;
    height: 660px;
    background: var(--card);
    border-radius: 26px;
    box-shadow: 0 18px 40px rgba(0,0,0,0.55);
    display: flex;
    flex-direction: column;
    align-items: center;
  }
  .card--front { left: 170px; }
  .card--back { left: 640px; justify-content: center; }

  .brand {
    display: flex;
    align-items: center;
    gap: 14px;
    color: var(--accent);
    font-weight: 700;
    font-size: 30px;
    line-height: 1.1;
  }
  .brand__dot {
    flex: none;
    width: 44px;
    height: 44px;
    border-radius: 50%;
    background: var(--accent);
  }
  .card--front .brand { margin-top: 150px; }

  .person {
    margin-top: 120px;
    text-align: center;
  }
  .person__name {
    color: var(--accent);
    font-weight: 700;
    font-size: 27px;
    letter-spacing: 1px;
  }
  .person__role {
    margin-top: 6px;
    color: var(--ink);
    font-size: 20px;
  }

  .icon-rule {
    margin-top: 14px;
    width: 340px;
    display: flex;
    align-items: center;
    gap: 8px;
  }
  .icon-rule__line {
    flex: 1;
    height: 2px;
    background: var(--accent-deep);
  }
  .icon-rule__icons {
    display: flex;
    gap: 6px;
  }
  .icon { width: 24px; height: 24px; display: block; }

  .contact {
    margin-top: 14px;
    list-style: none;
    text-align: center;
    color: var(--ink-soft);
    font-size: 19px;
    line-height: 1.35;
  }
</style>
</head>
<body>
<main class="sheet">
  <section class="card card--front" aria-label="Business card front">
    <div class="brand">
      <span class="brand__dot"></span>
      <span class="brand__name">Cascadia<br>Rhythm Guild</span>
    </div>

    <div class="person">
      <h1 class="person__name">JONATHAN SMITH</h1>
      <p class="person__role">Managing Director</p>
    </div>

    <div class="icon-rule">
      <span class="icon-rule__line"></span>
      <div class="icon-rule__icons">
        <svg class="icon" viewBox="0 0 24 24" aria-label="Phone">
          <circle cx="12" cy="12" r="12" fill="#e0461c"/>
          <path d="M8.5 6.5l2 2-1.2 1.6c.8 1.6 2 2.8 3.6 3.6l1.6-1.2 2 2-1.3 1.8c-4-.6-7.7-4.3-8.3-8.3z" fill="#fff"/>
        </svg>
        <svg class="icon" viewBox="0 0 24 24" aria-label="Email">
          <circle cx="12" cy="12" r="12" fill="#e0461c"/>
          <rect x="6" y="8" width="12" height="8" fill="#fff"/>
          <path d="M6 8l6 4.5L18 8" fill="none" stroke="#e0461c" stroke-width="1.2"/>
        </svg>
        <svg class="icon" viewBox="0 0 24 24" aria-label="Website">
          <circle cx="12" cy="12" r="12" fill="#e0461c"/>
          <circle cx="12" cy="12" r="6" fill="none" stroke="#fff" stroke-width="1.4"/>
          <path d="M6 12h12M12 6c-2.5 3-2.5 9 0 12M12 6c2.5 3 2.5 9 0 12" fill="none" stroke="#fff" stroke-width="1.2"/>
        </svg>
        <svg class="icon" viewBox="0 0 24 24" aria-label="Address">
          <circle cx="12" cy="12" r="12" fill="#e0461c"/>
          <path d="M12 5.5a4 4 0 0 1 4 4c0 3-4 8-4 8s-4-5-4-8a4 4 0 0 1 4-4z" fill="#fff"/>
          <circle cx="12" cy="9.6" r="1.5" fill="#e0461c"/>
        </svg>
      </div>
      <span class="icon-rule__line"></span>
    </div>

    <ul class="contact">
      <li>044-123 456 789</li>
      <li>info@webname.com</li>
      <li>www.websitename.com</li>
      <li>421, Address line goes here</li>
      <li>45452, Country name</li>
    </ul>
  </section>

  <section class="card card--back" aria-label="Business card back">
    <div class="brand">
      <span class="brand__dot"></span>
      <span class="brand__name">Cascadia<br>Rhythm Guild</span>
    </div>
  </section>
</main>
</body>
</html>
```